Postcard design to acquire new clients for my Property Management Company

I'm looking for a postcard design that I can send to prospective clients detailing information about my company and services.
Postcard should be eye catching and contain information from www.brightkeyrentals-example.com. I've provided a few screen shots for the most important information and my logo.
Target Market(s)
Real Estate
Industry/Entity Type
Real Estate
Font styles to use
Sans Serif
Requirements
Must have
- Must be eye catching!! this will be a direct mail piece - I'd like for the card to be read and not tossed in the trash immediately.
Design que from the logo.
A place to write / print the receipts name and address.
our physical address - 2287 Marble Lane, Lubbock, TX 79555.
Should not have
- the contact information on the business card is not accurate - please use info from website.

```html
<!DOCTYPE html>
<html lang="en">
<head>
<meta charset="utf-8">
<title>BrightKey Property Management – Postcard</title>
<link rel="stylesheet" href="https://fonts.googleapis.com/css2?family=Montserrat:wght@400;500;600;700;800&display=swap">
<style>
  :root {
    --stage: #2a2625;
    --brand-blue: #0a4a7f;
    --ink: #1e1e1e;
    --paper: #f4f4f4;
    --paper-soft: #e9eaeb;
    --white: #ffffff;
    --rule: #8a8a8a;
    --photo-sky: #c9d6e4;
    --photo-brick: #7b4c3c;
    --photo-grass: #4f7f35;
    --dusk-top: #4d5a6c;
    --dusk-bottom: #6a4a3c;
  }
  * { box-sizing: border-box; margin: 0; padding: 0; }
  html, body { width: 1024px; height: 1200px; overflow: hidden; background: var(--stage); }
  body { font-family: "Montserrat", Arial, sans-serif; }
  .stage { position: relative; width: 1000px; height: 1172px; transform: scale(1.024); transform-origin: 0 0; }

  .card { position: absolute; left: 98px; width: 803px; height: 443px; overflow: hidden; box-shadow: 0 10px 24px rgba(0,0,0,.45); }
  .card--front { top: 84px; background: linear-gradient(135deg, var(--white) 0%, var(--paper) 55%, var(--paper-soft) 100%); }
  .card--back { top: 607px; background: var(--paper); }

  /* front */
  .brand { position: absolute; left: 42px; top: 40px; color: var(--brand-blue); font-weight: 700; }
  .brand__name { font-size: 21px; letter-spacing: 2.5px; line-height: 1; }
  .brand__sub { font-size: 9.5px; letter-spacing: 1.6px; margin-top: 4px; }

  .headline-band { position: absolute; left: 0; top: 108px; width: 410px; height: 180px;
    background: linear-gradient(90deg, var(--brand-blue) 0%, var(--brand-blue) 88%, rgba(10,74,127,.55) 100%); }
  .headline { position: absolute; left: 43px; top: 128px; color: var(--white); font-weight: 800; font-size: 35px; line-height: 36px; letter-spacing: .3px; }

  .testimonial { position: absolute; left: 49px; top: 302px; width: 326px; font-size: 10.2px; line-height: 14px; color: var(--ink); }
  .reviewer { position: absolute; left: 49px; top: 372px; display: flex; align-items: center; gap: 12px; }
  .reviewer__photo { width: 40px; height: 40px; border-radius: 50%; background: radial-gradient(circle at 50% 40%, #c9a58c 0%, #3a3a44 70%); border: 2px solid var(--white); }
  .reviewer__name { font-size: 9.5px; font-weight: 700; color: var(--brand-blue); }
  .reviewer__role { font-size: 9.5px; font-weight: 500; color: var(--brand-blue); letter-spacing: .4px; margin-top: 2px; }
  .testimonial-rule { position: absolute; left: 49px; top: 422px; width: 154px; height: 1px; background: var(--ink); }

  .plan { position: absolute; left: 400px; width: 109px; height: 108px; background: var(--white); border-radius: 6px;
    box-shadow: 0 3px 8px rgba(0,0,0,.22); text-align: center; }
  .plan__label { display: block; margin: 14px 0 0 0; height: 20px; border-radius: 0 10px 10px 0; background: var(--brand-blue);
    color: var(--white); font-size: 12px; line-height: 20px; width: 101px; }
  .plan__rate { font-size: 29px; font-weight: 700; color: var(--brand-blue); margin-top: 6px; line-height: 34px; }
  .plan__note { font-size: 9.5px; color: var(--ink); margin-top: 4px; }
  .plan--lease { top: 39px; } .plan--full { top: 164px; } .plan--premium { top: 289px; }

  .house-photo { position: absolute; left: 522px; top: 0; width: 281px; height: 443px;
    background: linear-gradient(180deg, var(--photo-sky) 0%, #e3e9f0 28%, var(--photo-brick) 52%, #5c4a3e 66%, var(--photo-grass) 78%, #3f6a2b 100%); }
  .front-contact { position: absolute; left: 522px; top: 329px; width: 281px; height: 93px; background: var(--brand-blue); color: var(--white); }
  .front-contact__phone { position: absolute; left: 16px; top: 13px; display: flex; align-items: center; gap: 9px; font-size: 25px; font-weight: 500; letter-spacing: .8px; }
  .front-contact__web { position: absolute; left: 0; width: 100%; top: 50px; text-align: center; font-size: 12px; letter-spacing: .6px; }
  .front-contact__address { position: absolute; left: 0; width: 100%; top: 70px; text-align: center; font-size: 10.5px; letter-spacing: .4px; }

  .phone-icon { display: block; }

  /* back */
  .city-photo { position: absolute; left: 0; top: 0; width: 522px; height: 443px;
    background: linear-gradient(180deg, var(--dusk-top) 0%, #56606e 45%, #5a5048 75%, var(--dusk-bottom) 100%); }
  .services-title { position: absolute; left: 41px; top: 33px; color: var(--white); font-weight: 800; font-size: 37px; line-height: 39px; }
  .services { position: absolute; list-style: none; color: var(--white); font-size: 15.5px; }
  .services li { height: 37.5px; display: flex; gap: 10px; }
  .services--left { left: 41px; top: 137px; }
  .services--right { left: 282px; top: 140px; }
  .tick { font-size: 13px; }

  .address-side { position: absolute; left: 522px; top: 0; width: 281px; height: 443px; background: linear-gradient(160deg, var(--white) 0%, var(--paper) 60%, var(--paper-soft) 100%); }
  .stamp-box { position: absolute; left: 155px; top: 38px; width: 88px; height: 88px; border: 1.5px solid var(--rule); background: var(--white); }
  .address-line { position: absolute; left: 17px; width: 226px; height: 1px; background: var(--rule); }

  .cta-band { position: absolute; left: 0; top: 320px; width: 803px; height: 105px; background: var(--brand-blue); color: var(--white); }
  .cta-title { position: absolute; left: 41px; top: 10px; font-weight: 800; font-size: 35px; line-height: 39px; }
  .cta-contact__phone { position: absolute; left: 464px; top: 18px; display: flex; align-items: center; gap: 9px; font-size: 30px; font-weight: 500; letter-spacing: 1px; }
  .cta-contact__email { position: absolute; left: 464px; width: 320px; top: 61px; text-align: center; font-size: 14px; letter-spacing: .6px; }
</style>
</head>
<body>
<svg width="0" height="0" style="position:absolute">
  <symbol id="icon-phone" viewBox="0 0 32 32">
    <circle cx="16" cy="16" r="14" fill="none" stroke="currentColor" stroke-width="2.4"/>
    <path d="M11.2 8.5l2.6-.4 1.6 4-1.8 1.4c.9 2 2.4 3.6 4.4 4.6l1.5-1.8 4 1.6-.4 2.7c-.2.9-1 1.4-1.9 1.3-5.6-.8-10-5.2-10.8-10.9-.1-1 .4-2.3 .8-2.5z" fill="currentColor"/>
  </symbol>
</svg>

<main class="stage">
  <section class="card card--front" aria-label="Postcard front">
    <div class="brand">
      <div class="brand__name">BRIGHTKEY</div>
      <div class="brand__sub">PROPERTY MANAGEMENT</div>
    </div>

    <div class="headline-band"></div>
    <h1 class="headline">CHOOSE THE<br>RIGHT PROPERTY<br>MANAGEMENT<br>SYSTEM</h1>

    <p class="testimonial">"Marla in the office was great. My mom was not understanding her rent amount so she set down with us and went over everything step by step. Most people don't go above and beyond anymore but she did."</p>
    <div class="reviewer">
      <div class="reviewer__photo" role="img" aria-label="Portrait photo of the reviewing customer"></div>
      <div>
        <div class="reviewer__name">Dennis R.</div>
        <div class="reviewer__role">Proud Customer</div>
      </div>
    </div>
    <div class="testimonial-rule"></div>

    <div class="plan plan--lease"><span class="plan__label">Lease Only</span><div class="plan__rate">9%</div><div class="plan__note">of annual lease</div></div>
    <div class="plan plan--full"><span class="plan__label">Full Service</span><div class="plan__rate">10%</div><div class="plan__note">of annual lease</div></div>
    <div class="plan plan--premium"><span class="plan__label">Premium</span><div class="plan__rate">12%</div><div class="plan__note">of annual lease</div></div>

    <div class="house-photo" role="img" aria-label="Photo of a large brick two-storey house with a green lawn under a cloudy sky"></div>
    <div class="front-contact">
      <div class="front-contact__phone"><svg class="phone-icon" width="28" height="28"><use href="#icon-phone"/></svg>(806) 555-0147</div>
      <div class="front-contact__web">www.brightkeyrentals-example.com</div>
      <div class="front-contact__address">2287 Marble Lane, Lubbock, TX 79555</div>
    </div>
  </section>

  <section class="card card--back" aria-label="Postcard back">
    <div class="city-photo" role="img" aria-label="Dusk photo of a city street with brick buildings and a streetlight"></div>
    <h2 class="services-title">DISCOVER OUR<br>SERVICES</h2>
    <ul class="services services--left">
      <li><span class="tick">✓</span>Property Marketing</li>
      <li><span class="tick">✓</span>Rent Collection</li>
      <li><span class="tick">✓</span>Property Inspections</li>
      <li><span class="tick">✓</span>Evictions</li>
    </ul>
    <ul class="services services--right">
      <li><span class="tick">✓</span>Tenant Screening</li>
      <li><span class="tick">✓</span>Maintenance</li>
      <li><span class="tick">✓</span>Financial Reporting</li>
      <li><span class="tick">✓</span>Legal Guidance</li>
    </ul>

    <div class="address-side">
      <div class="stamp-box"></div>
      <div class="address-line" style="top:186px"></div>
      <div class="address-line" style="top:224px"></div>
      <div class="address-line" style="top:261px"></div>
    </div>

    <div class="cta-band">
      <h2 class="cta-title">GET A FREE<br>RENTAL ANALYSIS</h2>
      <div class="cta-contact__phone"><svg class="phone-icon" width="36" height="36"><use href="#icon-phone"/></svg>(806) 555-0147</div>
      <div class="cta-contact__email">info@brightkeyrentals-example.com</div>
    </div>
  </section>
</main>
</body>
</html>
```